College Advising Business Card Design

We need a business card design for a new company. We advise students and their families on finding the right colleges to apply to; the application process; creating resumes; writing essays; and once students are accepted, figuring out what the best fit is. We pride ourselves on highly personal service, and we travel the country to learn about schools. The visual we have used on our website is a picture of a graduation caps tossed into the blue sky. See my website.

Target Market(s)

Parents of high school students

Industry/Entity Type

Travel

Contact Information for Business Card

COLLEGE IS THE DREAM. LET US HELP YOU FIND THE DESTINATION.

Marta Delvecchi Ornbrook and Associates
College Admissions Advising and Essay Guidance
enroll@martadelvecchiornbrook.example
555-418-PATH (7284)
Follow us on Friendline

```html
<!DOCTYPE html>
<html lang="en">
<head>
<meta charset="utf-8">
<title>Marta Delvecchi Ornbrook and Associates – Business Card</title>
<link rel="stylesheet" href="https://fonts.googleapis.com/css2?family=Arimo:wght@400;700&family=Cormorant+Garamond:ital,wght@1,600&display=swap">
<style>
  :root {
    --stage: #2a2a2a;
    --card-black: #0b0b0c;
    --brand-blue: #1e8fd8;
    --icon-blue: #1b86cf;
    --text-white: #ffffff;
    --sky-top: #2f8fd6;
    --sky-mid: #5cb0ea;
    --sky-light: #a9d6f5;
    --edge-blue: #47a7e6;
  }
  * { box-sizing: border-box; margin: 0; padding: 0; }
  html, body {
    width: 1200px; height: 900px; overflow: hidden;
    background: var(--stage);
    font-family: "Arimo", Arial, sans-serif;
  }
  .stage {
    position: relative; width: 1200px; height: 900px;
    display: flex; flex-direction: column; align-items: center; justify-content: center; gap: 30px;
  }
  .card {
    position: relative; width: 700px; height: 400px;
    background: var(--card-black);
    border-radius: 22px; overflow: hidden;
  }
  .sky-photo {
    position: absolute; left: 0; right: 0;
    background: linear-gradient(200deg, var(--sky-top) 0%, var(--sky-mid) 55%, var(--sky-light) 100%);
  }
  .brand-block { position: absolute; top: 20px; }
  .brand-name {
    color: var(--brand-blue); font-weight: 700; font-size: 21px;
    letter-spacing: 1px; text-transform: uppercase; line-height: 1; white-space: nowrap;
  }
  .tagline {
    color: var(--text-white); font-weight: 700; font-size: 12.5px;
    letter-spacing: 0.5px; text-transform: uppercase; margin-top: 6px; white-space: nowrap;
  }
  .edge-line { position: absolute; left: 0; width: 700px; pointer-events: none; }

  /* Front */
  .card-front .brand-block { left: 36px; }
  .card-front .sky-photo {
    top: 80px; height: 210px;
    clip-path: polygon(0 0, 100% 0, 100% 62%, 0 100%);
  }
  .card-front .edge-line { top: 80px; height: 210px; }
  .service-line {
    position: absolute; left: 0; right: 0; bottom: 40px;
    text-align: center; color: var(--text-white);
    font-family: "Cormorant Garamond", Georgia, serif; font-style: italic; font-weight: 600;
    font-size: 36px; letter-spacing: 0.5px; white-space: nowrap;
  }

  /* Back */
  .card-back .brand-block { right: 36px; text-align: right; }
  .card-back .sky-photo {
    top: 80px; height: 170px;
    clip-path: polygon(0 0, 100% 0, 100% 70.6%, 0 100%);
  }
  .card-back .edge-line { top: 80px; height: 170px; }
  .contact-list { position: absolute; list-style: none; }
  .contact-list li {
    display: flex; align-items: center; gap: 12px;
    color: var(--text-white); font-size: 17px; height: 30px; margin-bottom: 10px;
    white-space: nowrap;
  }
  .contact-icon { width: 30px; height: 30px; flex: none; }
  .contact-online { right: 40px; top: 244px; }
  .contact-primary { left: 40px; top: 320px; }
</style>
</head>
<body>
<main class="stage">

  <section class="card card-front" aria-label="Card front">
    <div class="sky-photo" role="img" aria-label="Photo of graduation caps tossed into a blue sky with white clouds"></div>
    <svg class="edge-line" viewBox="0 0 700 210" aria-hidden="true">
      <line x1="0" y1="1" x2="700" y2="1" stroke="var(--edge-blue)" stroke-width="2"/>
      <line x1="0" y1="209" x2="700" y2="130" stroke="var(--edge-blue)" stroke-width="2"/>
    </svg>
    <div class="brand-block">
      <h1 class="brand-name">Marta Delvecchi Ornbrook and Associates</h1>
      <p class="tagline">College is the dream. Let us help you find the destination.</p>
    </div>
    <p class="service-line">College Admissions Advising and Essay Guidance</p>
  </section>

  <section class="card card-back" aria-label="Card back">
    <div class="sky-photo" role="img" aria-label="Photo of graduation caps tossed into a blue sky with white clouds"></div>
    <svg class="edge-line" viewBox="0 0 700 170" aria-hidden="true">
      <line x1="0" y1="1" x2="700" y2="1" stroke="var(--edge-blue)" stroke-width="2"/>
      <line x1="0" y1="169" x2="700" y2="120" stroke="var(--edge-blue)" stroke-width="2"/>
    </svg>
    <div class="brand-block">
      <h2 class="brand-name">Marta Delvecchi Ornbrook and Associates</h2>
      <p class="tagline">College is the dream. Let us help you find the destination.</p>
    </div>

    <ul class="contact-list contact-online">
      <li>
        <svg class="contact-icon" viewBox="0 0 30 30" aria-hidden="true">
          <circle cx="15" cy="15" r="14" fill="var(--icon-blue)"/>
          <g fill="none" stroke="#0b0b0c" stroke-width="1.6">
            <circle cx="15" cy="15" r="8"/>
            <ellipse cx="15" cy="15" rx="3.5" ry="8"/>
            <line x1="7" y1="15" x2="23" y2="15"/>
            <line x1="8.5" y1="11" x2="21.5" y2="11"/>
            <line x1="8.5" y1="19" x2="21.5" y2="19"/>
          </g>
        </svg>
        www.martadelvecchiornbrook.example
      </li>
      <li>
        <svg class="contact-icon" viewBox="0 0 30 30" aria-hidden="true">
          <circle cx="15" cy="15" r="14" fill="var(--icon-blue)"/>
        </svg>
        Follow us on Friendline
      </li>
    </ul>

    <ul class="contact-list contact-primary">
      <li>
        <svg class="contact-icon" viewBox="0 0 30 30" aria-hidden="true">
          <circle cx="15" cy="15" r="14" fill="var(--icon-blue)"/>
          <path d="M10.5 8.5l2.6-.6 1.5 3.4-1.7 1.2c.8 1.8 2 3 3.8 3.8l1.2-1.7 3.4 1.5-.6 2.6c-5.5.3-10.5-4.7-10.2-10.2z" fill="#0b0b0c"/>
        </svg>
        555-418-PATH (7284)
      </li>
      <li>
        <svg class="contact-icon" viewBox="0 0 30 30" aria-hidden="true">
          <circle cx="15" cy="15" r="14" fill="var(--icon-blue)"/>
          <rect x="8" y="10" width="14" height="10" rx="1" fill="#0b0b0c"/>
          <path d="M8.5 10.5l6.5 5 6.5-5" fill="none" stroke="var(--icon-blue)" stroke-width="1.4"/>
        </svg>
        enroll@martadelvecchiornbrook.example
      </li>
    </ul>
  </section>

</main>
</body>
</html>
```